Stellan App | Pre-Launch Homepage

Dear designer,
Stellan is a soon to be launched innovative & free social platform for collaborative addictions quitting.
We require a design for our pre-launch homepage that will elevate our basic wireframes to the next level.
We would like the wireframes to serve as a guideline only, and not as a final version of the design. If you have cool ideas - we would appreciate your creativity!
* This is a pre-launch website for a mobile app, and as such the design must be consistent with the general style, design and atmosphere of the app (see screenshot in the shared Drive link).
* We liked the style and feel of the following website: http://plumvane.com/ - Please let's use it as a reference as well.
* The existing text in the wireframes is there just to represent a place for text. Copy will be edited by us after the design is done.
Please find the wireframes attached, and all relevant design assets and app screenshots in the following Drive shared link -
https://files.orbelink.com/open?id=7K204XqR3tPmHc8Lw2Jd61VnaGzT
Thanks,
Marcus
Industry/Entity Type
Social
Number of Pages Required
1 page
Look and feel
Each slider illustrates characteristics of the customer's brand and the style your logo design should communicate.

```html
<!DOCTYPE html>
<html lang="en">
<head>
<meta charset="utf-8">
<title>Stellan App | Pre-Launch Homepage</title>
<link rel="stylesheet" href="https://fonts.googleapis.com/css2?family=Montserrat:wght@400;600;700&family=Open+Sans:wght@400;600&display=swap">
<style>
  :root {
    --hero-dark: #23262e;
    --hero-mid: #3b3d4a;
    --teal: #3fd6b2;
    --teal-dark: #2aa98b;
    --coral: #f0545c;
    --lime: #d8e64b;
    --sky: #8ed7ec;
    --paper: #ffffff;
    --mist: #f3f4f5;
    --ink: #2c3238;
    --ink-soft: #8a9096;
    --deep-green: #1f5f52;
    --gold: #f2c230;
    --social-blue: #3b5b98;
    --social-red: #d9423a;
    --social-sky: #35a9e0;
  }
  * { box-sizing: border-box; margin: 0; padding: 0; }
  html, body { width: 1200px; height: 3300px; overflow: hidden; }
  body { position: relative; background: var(--paper); font-family: "Open Sans", sans-serif; color: var(--ink); }
  .section { position: absolute; left: 0; width: 1200px; overflow: hidden; }
  .heading { font-family: "Montserrat", sans-serif; font-weight: 700; }

  /* Hero */
  .hero { top: 0; height: 620px; }
  .hero-backdrop { position: absolute; inset: 0; background: radial-gradient(ellipse at 72% 55%, #6a5a58 0%, var(--hero-mid) 35%, var(--hero-dark) 80%); }
  .brand { position: absolute; left: 40px; top: 14px; font-family: "Montserrat", sans-serif; font-weight: 600; font-size: 46px; color: var(--paper); display: flex; align-items: center; gap: 12px; }
  .brand-dot { width: 14px; height: 14px; border-radius: 50%; background: var(--paper); }
  .tagline { position: absolute; left: 44px; top: 78px; font-size: 15px; color: var(--paper); }
  .contact-btn { position: absolute; left: 900px; top: 46px; width: 112px; height: 36px; background: var(--teal); color: var(--paper); font-family: "Montserrat", sans-serif; font-size: 11px; font-weight: 700; display: flex; align-items: center; justify-content: center; gap: 6px; border-radius: 3px; }
  .hero-headline { position: absolute; left: 150px; top: 266px; width: 480px; text-align: center; font-family: "Montserrat", sans-serif; font-size: 23px; line-height: 36px; color: var(--lime); font-weight: 400; }
  .hero-note { position: absolute; left: 150px; top: 398px; width: 480px; text-align: center; font-size: 14px; color: var(--paper); }
  .signup { position: absolute; display: flex; height: 40px; }
  .signup-input { background: var(--paper); color: #9aa0a6; font-size: 12px; display: flex; align-items: center; padding-left: 14px; }
  .signup-btn { background: var(--coral); color: var(--paper); font-family: "Montserrat", sans-serif; font-size: 12px; font-weight: 700; display: flex; align-items: center; justify-content: center; }
  .hero .signup { left: 160px; top: 448px; }
  .hero .signup-input { width: 282px; }
  .hero .signup-btn { width: 130px; }
  .hero-hand { position: absolute; left: 600px; top: 100px; width: 420px; height: 520px; border-radius: 200px 200px 0 0; background: radial-gradient(ellipse at 50% 70%, rgba(214,168,140,0.55), rgba(214,168,140,0) 70%); }
  .scroll-mouse { position: absolute; left: 589px; top: 570px; }

  /* Phone */
  .phone { position: absolute; border-radius: 26px; background: var(--paper); box-shadow: 0 0 0 2px #d9dde0; }
  .phone-screen { position: absolute; left: 9%; right: 9%; top: 12%; bottom: 12%; background: linear-gradient(#f6f7f8, #e7eaec); }
  .phone-speaker { position: absolute; left: 40%; right: 40%; top: 5.5%; height: 5px; border-radius: 3px; background: #cfd3d6; }
  .phone-home { position: absolute; left: 50%; bottom: 3%; width: 28px; height: 28px; margin-left: -14px; border-radius: 50%; border: 2px solid #cfd3d6; }
  .phone-badge { position: absolute; left: 50%; top: 50%; width: 64px; height: 64px; margin: -32px 0 0 -32px; border-radius: 50%; background: var(--coral); display: flex; align-items: center; justify-content: center; }

  /* Features */
  .features { top: 620px; height: 280px; background: var(--paper); }
  .feature { position: absolute; top: 40px; width: 240px; text-align: center; }
  .feature-icon { height: 70px; display: flex; justify-content: center; align-items: center; }
  .feature-title { margin-top: 26px; font-size: 16px; letter-spacing: 0.5px; }
  .feature-text { margin-top: 10px; font-size: 12px; line-height: 1.5; color: var(--ink-soft); padding: 0 30px; }

  .notch { position: absolute; left: 588px; top: -12px; width: 24px; height: 24px; border-radius: 50%; display: flex; align-items: center; justify-content: center; }

  /* Fun */
  .fun { top: 900px; height: 480px; background: var(--teal); }
  .vines { position: absolute; left: 300px; top: 40px; width: 320px; height: 400px; border-radius: 50%; background: radial-gradient(ellipse, rgba(255,255,255,0.0) 40%, rgba(240,200,90,0.35) 60%, rgba(255,255,255,0) 72%); }
  .section-title { font-size: 36px; }
  .copy { font-size: 13px; line-height: 1.6; }
  .fun .section-title { position: absolute; left: 690px; top: 180px; color: var(--ink); }
  .fun .copy-block { position: absolute; left: 690px; top: 240px; width: 400px; color: var(--deep-green); }
  .copy-block p + p { margin-top: 18px; }

  /* Inspire */
  .inspire { top: 1380px; height: 480px; background: var(--mist); }
  .inspire .section-title { position: absolute; left: 150px; top: 90px; width: 320px; text-align: center; }
  .inspire .copy-block { position: absolute; left: 150px; top: 150px; width: 320px; text-align: center; color: var(--ink-soft); }
  .network { position: absolute; left: 580px; top: 60px; width: 420px; height: 360px; border-radius: 50%; background: radial-gradient(ellipse, rgba(160,200,230,0.35), rgba(243,244,245,0) 70%); }

  /* Achieve */
  .achieve { top: 1860px; height: 540px; background: var(--sky); }
  .achieve .section-title { position: absolute; left: 0; width: 1200px; top: 50px; text-align: center; font-size: 30px; color: var(--ink); }
  .achieve .copy { position: absolute; left: 390px; width: 420px; top: 100px; text-align: center; color: var(--ink); font-size: 12px; }
  .achieve .copy-small { position: absolute; left: 0; width: 1200px; top: 172px; text-align: center; font-size: 11px; color: var(--ink); }
  .bubble { position: absolute; width: 250px; height: 74px; background: var(--paper); border-radius: 37px; display: flex; align-items: center; gap: 12px; padding: 0 18px 0 10px; }
  .bubble-icon { flex: none; width: 54px; height: 54px; border-radius: 50%; }
  .bubble-icon.trophy { background: var(--gold); }
  .bubble-icon.basket { background: var(--coral); }
  .bubble-text { font-size: 10.5px; line-height: 1.4; color: var(--ink); }

  /* Launch */
  .launch { top: 2400px; height: 900px; background: var(--paper); }
  .launch .section-title { position: absolute; left: 0; width: 1200px; top: 26px; text-align: center; font-size: 32px; }
  .stores { position: absolute; left: 530px; top: 455px; width: 140px; display: flex; justify-content: space-between; }
  .store-mark { width: 30px; height: 30px; border-radius: 6px; background: #9aa3aa; }
  .launch-note { position: absolute; left: 0; width: 1200px; top: 535px; text-align: center; font-size: 16px; }
  .launch .signup { left: 370px; top: 578px; }
  .launch .signup-input { width: 320px; border: 1px solid #dde0e3; }
  .launch .signup-btn { width: 140px; }
  .join-title { position: absolute; left: 0; width: 1200px; top: 665px; text-align: center; font-size: 16px; }
  .socials { position: absolute; left: 549px; top: 700px; display: flex; gap: 8px; }
  .social { width: 30px; height: 30px; border-radius: 50%; }
  .footer-copy { position: absolute; left: 0; width: 1200px; top: 786px; text-align: center; font-size: 10px; color: var(--ink-soft); }
  .footer-links { position: absolute; left: 0; width: 1200px; top: 806px; display: flex; justify-content: center; gap: 12px; font-size: 10px; color: var(--ink-soft); }
</style>
</head>
<body>

<header class="section hero">
  <div class="hero-backdrop" role="img" aria-label="Blurred dark photo of a hand holding a phone"></div>
  <div class="hero-hand" role="img" aria-label="Hand holding the phone"></div>
  <div class="brand"><span>Stellan</span><span class="brand-dot"></span></div>
  <p class="tagline">Become a Better Version of Yourself</p>
  <div class="contact-btn">
    <svg width="12" height="12" viewBox="0 0 24 24"><path fill="#fff" d="M6.6 10.8a15 15 0 0 0 6.6 6.6l2.2-2.2a1 1 0 0 1 1-.25 11.4 11.4 0 0 0 3.6.57 1 1 0 0 1 1 1V20a1 1 0 0 1-1 1A17 17 0 0 1 3 4a1 1 0 0 1 1-1h3.5a1 1 0 0 1 1 1c0 1.25.2 2.45.57 3.57a1 1 0 0 1-.25 1z"/></svg>
    CONTACT US
  </div>
  <h1 class="hero-headline">Stellan is a revolutionary &amp;<br>free social platform for<br>collaborative addictions quitting.</h1>
  <p class="hero-note">Subscribe below for the beta release and updates.</p>
  <div class="signup"><div class="signup-input">Enter your email address</div><div class="signup-btn">LET ME KNOW!</div></div>
  <div class="phone" style="left:680px;top:120px;width:180px;height:360px;">
    <div class="phone-speaker"></div>
    <div class="phone-screen" role="img" aria-label="App profile screen"></div>
    <div class="phone-home"></div>
  </div>
  <svg class="scroll-mouse" width="22" height="34" viewBox="0 0 22 34"><rect x="1" y="1" width="20" height="32" rx="10" fill="none" stroke="#fff" stroke-width="2"/><rect x="10" y="7" width="2" height="7" rx="1" fill="#fff"/></svg>
</header>

<section class="section features">
  <div class="feature" style="left:200px;">
    <div class="feature-icon">
      <svg width="64" height="64" viewBox="0 0 64 64"><circle cx="32" cy="32" r="26" fill="none" stroke="var(--coral)" stroke-width="12"/><circle cx="32" cy="32" r="26" fill="none" stroke="#fff" stroke-width="12" stroke-dasharray="14 27"/></svg>
    </div>
    <h3 class="feature-title heading">NEVER BE ALONE</h3>
    <p class="feature-text">Forget what you know - Stellan makes it fun to quit.</p>
  </div>
  <div class="feature" style="left:480px;">
    <div class="feature-icon">
      <svg width="68" height="66" viewBox="0 0 68 66"><polygon points="34,2 43,24 66,25 48,40 54,63 34,50 14,63 20,40 2,25 25,24" fill="var(--gold)"/></svg>
    </div>
    <h3 class="feature-title heading">NETWORK POWER</h3>
    <p class="feature-text">Forget what you know - Stellan makes it fun to quit.</p>
  </div>
  <div class="feature" style="left:760px;">
    <div class="feature-icon">
      <svg width="64" height="64" viewBox="0 0 64 64"><circle cx="32" cy="32" r="28" fill="none" stroke="#444" stroke-width="3"/><circle cx="32" cy="32" r="20" fill="none" stroke="#444" stroke-width="3"/><circle cx="32" cy="32" r="12" fill="none" stroke="#444" stroke-width="3"/><circle cx="32" cy="32" r="4" fill="#444"/></svg>
    </div>
    <h3 class="feature-title heading">STAY MOTIVATED</h3>
    <p class="feature-text">Forget what you know - Stellan makes it fun to quit.</p>
  </div>
</section>

<section class="section fun">
  <div class="notch" style="top:-10px;background:var(--teal);"><svg width="10" height="6" viewBox="0 0 10 6"><path d="M1 1l4 4 4-4" stroke="#fff" stroke-width="1.5" fill="none"/></svg></div>
  <div class="vines" role="img" aria-label="Leafy vines wrapping around the phone"></div>
  <div class="phone" style="left:375px;top:70px;width:170px;height:340px;">
    <div class="phone-speaker"></div>
    <div class="phone-screen"></div>
    <div class="phone-badge"><svg width="30" height="28" viewBox="0 0 30 28"><path d="M15 27S1 18 1 9a7 7 0 0 1 14-2 7 7 0 0 1 14 2c0 9-14 18-14 18z" fill="#fff"/></svg></div>
    <div class="phone-home"></div>
  </div>
  <h2 class="section-title heading">Fun</h2>
  <div class="copy-block copy">
    <p>Forget what you know - Stellan makes it fun to quit. The app turns your goal and daily wins into a game you share with friends and supporters.</p>
    <p>Stellan gives you the chance to earn points, unlock levels and cheer others on, so every smoke-free day feels like a small victory worth sharing.</p>
  </div>
</section>

<section class="section inspire">
  <div class="notch" style="top:-10px;background:var(--mist);"><svg width="10" height="6" viewBox="0 0 10 6"><path d="M1 1l4 4 4-4" stroke="var(--teal-dark)" stroke-width="1.5" fill="none"/></svg></div>
  <h2 class="section-title heading">Inspire</h2>
  <div class="copy-block copy">
    <p>One of the most important factors for successful quitting is the ability to stay inspired during the process.</p>
    <p>That's why we designed Stellan as a platform where you can inspire and be inspired by a supportive network of awesome quitters.</p>
  </div>
  <div class="network" role="img" aria-label="Network of connected people around the phone"></div>
  <div class="phone" style="left:680px;top:90px;width:170px;height:340px;">
    <div class="phone-speaker"></div>
    <div class="phone-screen"></div>
    <div class="phone-badge"><svg width="28" height="28" viewBox="0 0 28 28"><g fill="#fff"><circle cx="21" cy="6" r="4"/><circle cx="7" cy="14" r="4"/><circle cx="21" cy="22" r="4"/></g><path d="M21 6L7 14l14 8" stroke="#fff" stroke-width="2" fill="none"/></svg></div>
    <div class="phone-home"></div>
  </div>
</section>

<section class="section achieve">
  <div class="notch" style="top:-10px;background:var(--sky);"><svg width="10" height="6" viewBox="0 0 10 6"><path d="M1 1l4 4 4-4" stroke="#fff" stroke-width="1.5" fill="none"/></svg></div>
  <h2 class="section-title heading">Achieve</h2>
  <p class="copy">Stellan is built as a pyramid of relationships that makes use of the Social Cognitive Theory, to promote a supportive network of positive reinforcement.</p>
  <p class="copy-small">The bigger you make it, the stronger you get.</p>
  <div class="phone" style="left:520px;top:210px;width:160px;height:360px;">
    <div class="phone-speaker"></div>
    <div class="phone-screen"></div>
  </div>
  <div class="bubble" style="left:160px;top:280px;"><div class="bubble-icon trophy" role="img" aria-label="Trophy"></div><p class="bubble-text">Stellan is built as a pyramid of relationships that makes use of the Social Cognitive Theory</p></div>
  <div class="bubble" style="left:160px;top:390px;"><div class="bubble-icon basket" role="img" aria-label="Basket"></div><p class="bubble-text">Stellan is built as a pyramid of relationships that makes use of the Social Cognitive Theory</p></div>
  <div class="bubble" style="left:790px;top:280px;"><div class="bubble-icon trophy" role="img" aria-label="Trophy"></div><p class="bubble-text">Stellan is built as a pyramid of relationships that makes use of the Social Cognitive Theory</p></div>
  <div class="bubble" style="left:790px;top:390px;"><div class="bubble-icon basket" role="img" aria-label="Basket"></div><p class="bubble-text">Stellan is built as a pyramid of relationships that makes use of the Social Cognitive Theory</p></div>
</section>

<section class="section launch">
  <svg style="position:absolute;left:592px;top:-2px;" width="16" height="20" viewBox="0 0 16 20"><path d="M8 18V3M2 9l6-6 6 6" stroke="var(--ink)" stroke-width="2.5" fill="none"/></svg>
  <h2 class="section-title heading">Coming Soon</h2>
  <div class="phone" style="left:520px;top:110px;width:160px;height:320px;">
    <div class="phone-speaker"></div>
    <div class="phone-screen" role="img" aria-label="App profile screen"></div>
    <div class="phone-home"></div>
  </div>
  <div class="stores"><span class="store-mark"></span><span class="store-mark"></span><span class="store-mark"></span></div>
  <p class="launch-note heading">Subscribe below for the beta release and updates.</p>
  <div class="signup"><div class="signup-input">Enter your email address</div><div class="signup-btn">LET ME KNOW!</div></div>
  <p class="join-title heading">Join the revolution</p>
  <div class="socials"><span class="social" style="background:var(--social-blue)"></span><span class="social" style="background:var(--social-red)"></span><span class="social" style="background:var(--social-sky)"></span></div>
  <p class="footer-copy">Copyright © 2015 Stellan</p>
  <p class="footer-links"><span>Contact Us</span><span>|</span><span>T&amp;C's</span><span>|</span><span>Privacy Policy</span></p>
</section>

</body>
</html>
```